Business Card Design Project

We need a business card for our business called Our Harbour Lender. (www.ourharbourlender.com.au)

There are 3 of us in the business, the design we choose will stay the same for all 3 of us, but will need names changed and mobile numbers added. I will provide details in an attachment.

We are a professional services directory for mortgage brokers. I will attach an idea that I had, but happy for you to be free in your designs. We would like the colour scheme to remain within our company colours - blue, white, grey and orange.

Thanks so much for helping us with this project. If you need anymore information, please don't hesitate to ask.

Industry/Entity Type

Business

Requirements
Must have
• Our Harbour Lender Logo
Colour blue and orange to match closely with our logo samples if possible.
The most important card is the card for Mirel Dunphy

```html
<!DOCTYPE html>
<html lang="en">
<head>
<meta charset="utf-8">
<title>Our Harbour Lender – Business Card</title>
<link rel="stylesheet" href="https://fonts.googleapis.com/css2?family=Roboto:wght@300;400;700&display=swap">
<style>
  :root {
    --stage: #222222;
    --brand-blue: #2b87bf;
    --white: #ffffff;
    --card-light: #f2f2f2;
    --card-shade: #cdcdcd;
    --icon-dark: #222222;
  }
  * { box-sizing: border-box; margin: 0; padding: 0; }
  html, body {
    width: 955px; height: 1200px; overflow: hidden;
    background: var(--stage);
    font-family: "Roboto", Arial, sans-serif;
  }
  .canvas { position: relative; width: 955px; height: 1200px; }
  .card { position: absolute; left: 10px; width: 938px; height: 562px; }
  .card-front { top: 19px; background: var(--brand-blue); }
  .card-back {
    top: 628px;
    background: radial-gradient(ellipse 75% 90% at 32% 45%, var(--card-light) 0%, #e4e4e4 55%, var(--card-shade) 100%);
  }
  .wordmark {
    position: absolute; left: 0; right: 0; top: 232px;
    display: flex; align-items: center; justify-content: center; gap: 22px;
  }
  .wordmark-dot {
    width: 40px; height: 40px; border-radius: 50%; background: var(--white);
  }
  .wordmark-name {
    color: var(--white); font-weight: 400; font-size: 74px; letter-spacing: -1px; line-height: 1;
  }
  .person-name {
    position: absolute; left: 79px; top: 98px;
    color: var(--brand-blue); font-weight: 700; font-size: 56px; letter-spacing: 0.5px; line-height: 1;
  }
  .person-role {
    position: absolute; left: 80px; top: 156px;
    color: var(--brand-blue); font-weight: 300; font-size: 38px; line-height: 1;
  }
  .contact-list { position: absolute; left: 152px; top: 240px; list-style: none; }
  .contact-item {
    display: flex; align-items: center; height: 39px;
    color: var(--brand-blue); font-weight: 300; font-size: 25px;
  }
  .contact-icon { width: 32px; height: 28px; margin-right: 26px; flex: none; }
  .legal-note {
    position: absolute; left: 79px; top: 472px;
    color: var(--brand-blue); font-weight: 300; font-size: 19px; line-height: 24px;
  }
</style>
</head>
<body>
<main class="canvas">
  <section class="card card-front" aria-label="Card front">
    <div class="wordmark">
      <span class="wordmark-dot"></span>
      <span class="wordmark-name">Our Harbour Lender</span>
    </div>
  </section>

  <section class="card card-back" aria-label="Card back">
    <h1 class="person-name">MIREL DUNPHY</h1>
    <p class="person-role">CEO / FOUNDER</p>
    <ul class="contact-list">
      <li class="contact-item">
        <svg class="contact-icon" viewBox="0 0 32 28" aria-hidden="true"><path fill="var(--icon-dark)" d="M2 9c0-4 28-4 28 0v3h-7V9c-4-1-10-1-14 0v3H2z M9 12h14l5 11H4z"/><circle cx="16" cy="18" r="3" fill="#eee"/></svg>
        1300 HARBOUR
      </li>
      <li class="contact-item">
        <svg class="contact-icon" viewBox="0 0 32 28" aria-hidden="true"><rect x="10" y="2" width="12" height="25" rx="2" fill="var(--icon-dark)"/><rect x="12" y="5" width="8" height="8" fill="#eee"/><rect x="14" y="0" width="2" height="3" fill="var(--icon-dark)"/></svg>
        0400 555 218
      </li>
      <li class="contact-item">
        <svg class="contact-icon" viewBox="0 0 32 28" aria-hidden="true"><rect x="9" y="2" width="14" height="8" fill="var(--icon-dark)"/><rect x="3" y="9" width="26" height="12" rx="2" fill="var(--icon-dark)"/><rect x="8" y="18" width="16" height="8" fill="#eee" stroke="var(--icon-dark)" stroke-width="2"/></svg>
        02 5550 1942
      </li>
      <li class="contact-item">
        <svg class="contact-icon" viewBox="0 0 32 28" aria-hidden="true"><path fill="none" stroke="var(--icon-dark)" stroke-width="2.5" d="M4 11l12-8 12 8v14H4z M4 11l12 9 12-9"/></svg>
        mirel@harbourmail.com
      </li>
      <li class="contact-item">
        <svg class="contact-icon" viewBox="0 0 32 28" aria-hidden="true"><g fill="none" stroke="var(--icon-dark)" stroke-width="2"><circle cx="16" cy="14" r="12"/><ellipse cx="16" cy="14" rx="5" ry="12"/><path d="M4 14h24M6 8h20M6 20h20"/></g></svg>
        www.ourharbourlender.com.au
      </li>
    </ul>
    <p class="legal-note">Our Harbour Lender is a Tidewater Finance Group Pty Ltd project<br>ABN 41 200 555 017</p>
  </section>
</main>
</body>
</html>
```